Meadowlark Learning Growth Partners (MLGP)

This is a professional business card. Logo and picture are a must on the front of the card. I am an educational consultant. I have been consulting for the past three years for a company. I am now opening my own company. My goal for my consulting company is to eventually consult all over America.

Target Market(s)

Educators, schools, professionals

Industry/Entity Type

Consulting

Contact Information for Business Card

Picture/logo on front, simple modern design

Font styles to use
Serif

Colors
85abd2
0355a3
3176b5
cedeed

Requirements
Must have
• picture, logo,
• Odessa Pruitt, Ed.S
• address 5073 Cormorant ridge Dr. Nashville, TN 37940
• Cell:616-555-0148
• Office: 629-555-0172
• www.Mlgpedu.example
• pruittodessa@mailbox.example

```html
<!DOCTYPE html>
<html lang="en">
<head>
<meta charset="utf-8">
<title>Meadowlark Learning Growth Partners – Business Card</title>
<link href="https://fonts.googleapis.com/css2?family=Lora:wght@600;700&family=Source+Serif+4:wght@400;500&display=swap" rel="stylesheet">
<style>
  :root {
    --bg: #c9c9c9;
    --blue-strong: #0355a3;
    --blue-mid: #3176b5;
    --blue-light: #85abd2;
    --blue-pale: #cedeed;
    --card-glow: #1c5fa6;
    --card-core: #0a4687;
    --card-edge: #062c59;
    --ink: #ffffff;
  }
  * { box-sizing: border-box; margin: 0; padding: 0; }
  html, body { width: 1200px; height: 876px; overflow: hidden; }
  body {
    background: var(--bg);
    display: flex;
    align-items: center;
    justify-content: center;
    gap: 40px;
  }
  .card {
    width: 540px;
    height: 309px;
    border-radius: 3px;
    background: radial-gradient(ellipse at 40% 30%, var(--card-glow) 0%, var(--card-core) 48%, var(--card-edge) 100%);
    border-bottom: 4px solid var(--blue-mid);
    box-shadow: 0 10px 24px rgba(0,0,0,0.3);
    display: flex;
    align-items: center;
    color: var(--ink);
  }
  .brand-mark {
    display: flex;
    align-items: center;
    gap: 10px;
    font-family: "Lora", serif;
    font-weight: 700;
    font-size: 38px;
    letter-spacing: 1px;
    color: var(--ink);
  }
  .brand-dot {
    width: 15px; height: 15px;
    border-radius: 50%;
    background: var(--blue-light);
  }
  .divider {
    width: 1.5px;
    height: 120px;
    background: var(--blue-light);
    margin: 0 22px;
  }

  /* Front */
  .card-front { padding-left: 62px; }
  .company-name {
    font-family: "Lora", serif;
    font-weight: 600;
    font-size: 23px;
    line-height: 1.15;
    color: var(--ink);
  }

  /* Back */
  .card-back { padding-left: 30px; }
  .card-back .brand-mark { font-size: 28px; gap: 8px; }
  .card-back .brand-dot { width: 12px; height: 12px; }
  .card-back .divider { height: 160px; margin: 0 16px; }
  .contact-name {
    font-family: "Lora", serif;
    font-weight: 600;
    font-size: 21px;
    margin-bottom: 10px;
    white-space: nowrap;
  }
  .contact-name .credential {
    font-family: "Source Serif 4", serif;
    font-weight: 400;
    font-size: 13px;
    margin-left: 4px;
    color: var(--blue-pale);
  }
  .contact-list { list-style: none; }
  .contact-list li {
    display: flex;
    align-items: center;
    gap: 7px;
    font-family: "Source Serif 4", serif;
    font-size: 11.5px;
    color: var(--blue-pale);
    line-height: 1.6;
    white-space: nowrap;
  }
  .contact-list svg { width: 11px; height: 11px; flex: none; }
</style>
</head>
<body>

<section class="card card-front" aria-label="Business card front">
  <div class="brand-mark"><span class="brand-dot"></span>MLGP</div>
  <div class="divider"></div>
  <p class="company-name">Meadowlark<br>Learning<br>Growth<br>Partners</p>
</section>

<section class="card card-back" aria-label="Business card back">
  <div class="brand-mark"><span class="brand-dot"></span>MLGP</div>
  <div class="divider"></div>
  <div class="contact">
    <p class="contact-name">Odessa Pruitt,<span class="credential">Ed.S</span></p>
    <ul class="contact-list">
      <li>
        <svg viewBox="0 0 12 12" fill="none" stroke="#85abd2" stroke-width="1.3"><rect x="3" y="0.8" width="6" height="10.4" rx="1"/><line x1="5" y1="9.4" x2="7" y2="9.4"/></svg>
        Cell: 616-555-0148
      </li>
      <li>
        <svg viewBox="0 0 12 12" fill="#85abd2"><path d="M2.4 1l2 .2.9 2.4-1.2 1a7 7 0 0 0 3.3 3.3l1-1.2 2.4.9.2 2A1.4 1.4 0 0 1 9.6 11 8.6 8.6 0 0 1 1 2.4 1.4 1.4 0 0 1 2.4 1z"/></svg>
        Office: 629-555-0172
      </li>
      <li>
        <svg viewBox="0 0 12 12"><path d="M1 2.5h10v7H1z" fill="#85abd2"/><path d="M1 2.5l5 4 5-4" stroke="#0a4687" stroke-width="1" fill="none"/></svg>
        pruittodessa@mailbox.example
      </li>
      <li>
        <svg viewBox="0 0 12 12" fill="none" stroke="#85abd2" stroke-width="1"><circle cx="6" cy="6" r="5"/><ellipse cx="6" cy="6" rx="2.2" ry="5"/><line x1="1" y1="6" x2="11" y2="6"/></svg>
        www.Mlgpedu.example
      </li>
      <li>
        <svg viewBox="0 0 12 12" fill="#85abd2"><path d="M6 0.6A3.9 3.9 0 0 0 2.1 4.5C2.1 7.6 6 11.4 6 11.4S9.9 7.6 9.9 4.5A3.9 3.9 0 0 0 6 0.6zm0 5.4a1.5 1.5 0 1 1 0-3 1.5 1.5 0 0 1 0 3z"/></svg>
        5073 Cormorant Ridge Dr., Nashville, TN 37940
      </li>
    </ul>
  </div>
</section>

</body>
</html>
```